Marrowgate Concepts/Innovation Consultant-One Page (for now) Site Reflective Of Its Focus.

Based in Tampa, Florida...I offer my consulting services, along with my extensive network of companies and technologies, to people that are looking for new, novel, and innovative applications for their technology and/or companies & governmental agencies to identify solutions to their Existing Challenges and Future Needs. I then Identify Connections and/or Solutions between technologies and set up collaborations between the parties. I also run a Forum that allows people to present new, novel, and innovative technologies and capabilities to a broad audience for ideation and collaboration.

Logo Text

Marrowgate Concepts LLC

Coding

```html
<!DOCTYPE html>
<html lang="en">
<head>
<meta charset="utf-8">
<title>Marrowgate Concepts LLC</title>
<link href="https://fonts.googleapis.com/css2?family=Montserrat:wght@500;600;700;800&family=Mulish:wght@400;600;700&display=swap" rel="stylesheet">
<style>
:root{
  --blue:#0a6cc2;
  --blue-dark:#0b3f86;
  --ink:#141414;
  --text:#444a55;
  --muted:#f4f4f5;
  --footer:#eef1f6;
  --circle:#eef0f7;
  --white:#ffffff;
}
*{margin:0;padding:0;box-sizing:border-box}
html,body{width:1200px;height:3594px;overflow:hidden;background:var(--white)}
body{position:relative;font-family:'Mulish',sans-serif;color:var(--text)}
.abs{position:absolute}
.btn{position:absolute;background:var(--blue);color:var(--white);font-family:'Montserrat',sans-serif;font-weight:700;font-size:11px;display:flex;align-items:center;justify-content:center;letter-spacing:.2px}
h2.section-title{position:absolute;left:0;width:1200px;text-align:center;font-family:'Montserrat',sans-serif;font-weight:700;font-size:24px;color:var(--ink)}
.rule{position:absolute;height:3px;width:42px;background:var(--blue)}

/* header */
.site-header{position:absolute;left:0;top:0;width:1200px;height:67px;background:var(--white);z-index:2}
.brand{position:absolute;left:138px;top:22px;display:flex;align-items:center;gap:8px;font-family:'Montserrat',sans-serif;font-weight:700;font-size:15px;color:var(--blue-dark)}
.brand-mark{width:22px;height:22px;background:var(--blue-dark)}
.nav{position:absolute;top:24px;left:632px;display:flex;gap:0;font-family:'Mulish',sans-serif;font-weight:600;font-size:13px;color:#222}
.nav a{text-decoration:none;color:#222;padding:3px 8px;margin-right:16px}
.nav a.active{background:var(--blue);color:var(--white)}

/* hero */
.hero{position:absolute;left:0;top:67px;width:1200px;height:603px;background:linear-gradient(120deg,#5d83b3 0%,#a9c4e0 35%,#dbe7f3 55%,#7fa3cf 78%,#4f78ad 100%)}
.hero h1{position:absolute;top:98px;width:1200px;text-align:center;font-family:'Montserrat',sans-serif;font-weight:700;font-size:41px;color:#0f3a78}
.hero p{position:absolute;top:156px;left:300px;width:600px;text-align:center;font-size:17px;line-height:23px;color:#14233c}

/* services */
.card{position:absolute;width:455px;height:234px;background:var(--white);box-shadow:0 2px 14px rgba(0,0,0,.08)}
.card .icon{position:absolute;left:34px;top:36px;width:104px;height:104px;border-radius:50%;background:var(--circle);display:flex;align-items:center;justify-content:center}
.card h3{position:absolute;left:174px;top:30px;width:250px;font-family:'Montserrat',sans-serif;font-weight:500;font-size:15px;line-height:21px;color:var(--ink)}
.card p{position:absolute;left:176px;top:83px;width:250px;font-size:12px;line-height:15px;color:var(--text)}
.card .btn{left:177px;top:173px;width:88px;height:27px}
.stripes{position:absolute;width:52px;height:48px;background:repeating-linear-gradient(180deg,#dde1e8 0 1px,transparent 1px 6px)}

/* welcome */
.welcome{position:absolute;left:0;top:1333px;width:1200px;height:427px;background:var(--muted);overflow:hidden}
.welcome-photo{position:absolute;left:0;top:0;width:1200px;height:427px;clip-path:polygon(620px 0,1200px 0,1200px 427px,565px 427px);background:linear-gradient(160deg,#d7e0ea 0%,#9fb2c7 45%,#556a82 80%,#38465a 100%)}
.welcome-edge{position:absolute;left:0;top:0;width:1200px;height:427px;clip-path:polygon(608px 0,620px 0,565px 427px,553px 427px);background:var(--white)}
.block-title{position:absolute;font-family:'Montserrat',sans-serif;font-weight:700;font-size:23px;line-height:33px;color:var(--ink)}
.body-copy{position:absolute;font-size:14px;line-height:19.2px;color:var(--text)}

/* gov */
.gov-photo{position:absolute;left:132px;top:1814px;width:529px;height:393px;background:radial-gradient(circle at 50% 45%,#cfe3ea 0%,#7fa4b3 35%,#3f6675 70%,#2c4a57 100%)}

/* integration */
.integration{position:absolute;left:0;top:2255px;width:1200px;height:397px;background:radial-gradient(ellipse at 60% 60%,#1d5a88 0%,#0d3358 45%,#06162b 100%)}
.integration h2{position:absolute;top:112px;width:1200px;text-align:center;font-family:'Montserrat',sans-serif;font-weight:700;font-size:25px;color:var(--white)}
.integration p{position:absolute;top:156px;left:290px;width:620px;text-align:center;font-size:16px;line-height:23px;color:#e8f0fa}

/* blog */
.post{position:absolute;top:2770px;width:295px;height:445px;background:var(--white);box-shadow:0 2px 14px rgba(0,0,0,.08)}
.post .thumb{height:178px}
.post .date{position:absolute;left:29px;top:204px;font-size:11px;color:#333}
.post h3{position:absolute;left:29px;top:228px;width:245px;font-family:'Montserrat',sans-serif;font-weight:500;font-size:15.5px;line-height:22px;color:var(--ink)}
.post p{position:absolute;left:29px;top:285px;width:240px;font-size:12px;line-height:17.5px;color:var(--text)}
.post .btn{left:29px;top:383px;width:95px;height:29px;font-family:'Mulish',sans-serif;font-size:12px}
.dots{position:absolute;background-image:radial-gradient(circle,#c9ced8 1.6px,transparent 2px);background-size:13px 13px}

/* footer */
.site-footer{position:absolute;left:0;top:3250px;width:1200px;height:344px;background:var(--footer)}
.footer-brand{position:absolute;left:135px;top:105px;display:flex;align-items:center;gap:8px;font-family:'Montserrat',sans-serif;font-weight:700;font-size:15px;color:var(--blue-dark)}
.footer-col h4{position:absolute;top:45px;font-family:'Montserrat',sans-serif;font-weight:700;font-size:13px;color:#222}
.footer-col .line{position:absolute;top:68px;height:2px;background:#c7d3e3}
.f-item{position:absolute;display:flex;align-items:flex-start;gap:12px;font-size:12px;line-height:16px;color:#333}
.f-icon{width:22px;height:22px;border-radius:50%;background:var(--blue-dark);flex:none;margin-top:2px;display:flex;align-items:center;justify-content:center}
.menu-list{position:absolute;left:700px;top:88px;font-size:12px;line-height:17.5px;color:#333;list-style:none}
.footer-divider{position:absolute;left:130px;top:285px;width:940px;height:1px;background:#c9d0da}
.copyright{position:absolute;top:308px;width:1200px;text-align:center;font-size:12px;color:#333}
</style>
</head>
<body>

<header class="site-header">
  <div class="brand"><span class="brand-mark"></span>Marrowgate Concepts LLC</div>
  <nav class="nav">
    <a class="active">HOME</a><a>ABOUT US</a><a>SERVICES</a><a>BLOG</a><a>CONTACT US</a>
  </nav>
</header>

<section class="hero" role="img" aria-label="Business person typing on a laptop with overlaid network and data graphics">
  <h1>Innovative Consulting Services</h1>
  <p>Lorem ipsum dolor sit amet, consectetur adipiscing elit, sed do eiusmod tempor incididunt ut labore et dolore magna.</p>
  <div class="btn" style="left:541px;top:226px;width:118px;height:39px;font-size:13px">READ MORE</div>
</section>

<h2 class="section-title" style="top:707px">OUR SERVICES</h2>
<div class="rule" style="left:579px;top:752px"></div>
<div class="stripes" style="left:80px;top:822px"></div>
<div class="stripes" style="left:1068px;top:1183px"></div>

<article class="card" style="left:130px;top:788px">
  <div class="icon"><svg width="54" height="54" viewBox="0 0 54 54" fill="none" stroke="#0a6cc2" stroke-width="2"><path d="M27 8a14 14 0 0 0-8 25v6h16v-6a14 14 0 0 0-8-25z"/><path d="M21 43h12M23 47h8"/><path d="M22 20h10v8H22zM27 20v8"/></svg></div>
  <h3>Technology and<br>Company Consulting</h3>
  <p>Lorem ipsum dolor sit amet, conse ctetur adipiscing elit, sed do eiusmod tempor incididunt ut labore et dolore magna ullamco laboris nisi ut aliquip ex ea commodo consequat</p>
  <div class="btn">READ MORE</div>
</article>
<article class="card" style="left:612px;top:788px">
  <div class="icon"><svg width="56" height="56" viewBox="0 0 56 56" fill="none" stroke="#0a6cc2" stroke-width="2"><circle cx="14" cy="16" r="6"/><path d="M11 16l2 2 4-4"/><path d="M34 20v-6M39 20v-9M44 20v-12M30 21h16"/><circle cx="24" cy="30" r="4"/><rect x="8" y="34" width="10" height="12"/><path d="M30 36h12v6M42 42a3 3 0 1 0 0 6"/></svg></div>
  <h3>Strategic Connections<br>and Collaborations</h3>
  <p>Lorem ipsum dolor sit amet, conse ctetur adipiscing elit, sed do eiusmod tempor incididunt ut labore et dolore magna ullamco laboris nisi ut aliquip ex ea commodo consequat</p>
  <div class="btn">READ MORE</div>
</article>
<article class="card" style="left:130px;top:1045px">
  <div class="icon"><svg width="56" height="56" viewBox="0 0 56 56" fill="none" stroke="#0a6cc2" stroke-width="2"><rect x="8" y="10" width="32" height="26"/><path d="M8 16h32"/><circle cx="36" cy="36" r="7"/><path d="M36 24v4M36 44v4M24 36h4M44 36h4M28 28l3 3M41 41l3 3"/><path d="M14 24h10M14 29h6"/></svg></div>
  <h3>Innovative Applications<br>for Technology</h3>
  <p>Lorem ipsum dolor sit amet, conse ctetur adipiscing elit, sed do eiusmod tempor incididunt ut labore et dolore magna ullamco laboris nisi ut aliquip ex ea commodo consequat</p>
  <div class="btn">READ MORE</div>
</article>
<article class="card" style="left:612px;top:1045px">
  <div class="icon"><svg width="56" height="56" viewBox="0 0 56 56" fill="none" stroke="#0a6cc2" stroke-width="2"><path d="M12 8h20l8 8v30H12z"/><path d="M32 8v8h8"/><path d="M17 20h10M17 25h8M17 30h6"/><circle cx="33" cy="34" r="7"/><path d="M38 39l8 8"/></svg></div>
  <h3>Identifying Solutions for Existing<br>Challenges and Future Needs</h3>
  <p>Lorem ipsum dolor sit amet, conse ctetur adipiscing elit, sed do eiusmod tempor incididunt ut labore et dolore magna ullamco laboris nisi ut aliquip ex ea commodo consequat</p>
  <div class="btn">READ MORE</div>
</article>

<section class="welcome">
  <div class="welcome-photo" role="img" aria-label="Two business people shaking hands in front of tall office windows"></div>
  <div class="welcome-edge"></div>
  <h2 class="block-title" style="left:132px;top:38px">WELCOME TO<br>MARROWGATE CONCEPTS</h2>
  <div class="rule" style="left:132px;top:115px"></div>
  <p class="body-copy" style="left:132px;top:142px;width:395px">Sed ut perspiciatis unde omnis iste natus error sit voluptatem accusantium doloremque laudantium, totam rem aperiam, eaque ipsa quae ab illo inventore veritatis et quasi architecto beatae vitae dicta sunt explicabo. Nemo enim ipsam voluptatem quia voluptas sit aspernatur aut odit aut fugit, sed quia consequuntur magni dolores eos qui ratione voluptatem sequi nesciunt. Neque porro quisquam est, qui dolorem ipsum quia dolor sit amet, consectetur, adipisci velit, sed quia non .</p>
  <div class="btn" style="left:133px;top:341px;width:88px;height:27px">READ MORE</div>
</section>

<div class="gov-photo" role="img" aria-label="Glowing light bulb surrounded by technology icons on a desk"></div>
<h2 class="block-title" style="left:705px;top:1828px;width:380px">GOVERNMENTAL AGENCY SOLUTIONS: ADDRESSING CHALLENGES AND DRIVING INNOVATION</h2>
<div class="rule" style="left:705px;top:1978px"></div>
<p class="body-copy" style="left:705px;top:2004px;width:365px">Sed ut perspiciatis unde omnis iste natus error sit voluptatem accusantium doloremque laudantium, totam rem aperiam, eaque ipsa quae ab illo inventore veritatis et quasi architecto beatae vitae dicta sunt explicabo. Nemo enim ipsam voluptatem quia voluptas sit aspernatur aut odit aut fugit, sed quia consequuntur magni dolores eos qui ratione voluptatem sequi</p>
<div class="btn" style="left:706px;top:2160px;width:88px;height:27px">READ MORE</div>

<section class="integration" role="img" aria-label="Dark blue digital particle wave background">
  <h2>TECHNOLOGY INTEGRATION AND OPTIMIZATION</h2>
  <p>Sed ut perspiciatis unde omnis iste natus error sit voluptatem accusantium doloremque laudantium, totam rem aperiam, eaque ipsa quae ab illo inventore veritatis et quasi architecto beatae vitae dicta sunt explicabo.</p>
  <div class="btn" style="left:557px;top:251px;width:86px;height:27px">READ MORE</div>
</section>

<h2 class="section-title" style="top:2688px">LATEST BLOG</h2>
<div class="rule" style="left:579px;top:2734px"></div>
<div class="dots" style="left:98px;top:2735px;width:95px;height:82px"></div>
<div class="dots" style="left:995px;top:3148px;width:95px;height:82px"></div>

<article class="post" style="left:130px">
  <div class="thumb" role="img" aria-label="Team meeting around an office table" style="background:linear-gradient(135deg,#c9c0b4,#7d7a78 55%,#3f4650)"></div>
  <div class="date">27 June 2023</div>
  <h3>Lorem ipsum dolor sit amet consectetur adipiscing</h3>
  <p>Sed ut perspiciatis unde omnis iste natus error sit voluptatem accusantium doloremque laudantium, totam rem aperiam, eaque ipsa quae ab illo inventore veritatis.</p>
  <div class="btn">Read More</div>
</article>
<article class="post" style="left:453px">
  <div class="thumb" role="img" aria-label="Hands typing on a laptop with floating interface icons" style="background:linear-gradient(135deg,#dfe7ef,#a9b9c9 55%,#6d7f92)"></div>
  <div class="date">27 June 2023</div>
  <h3>Lorem ipsum dolor sit amet consectetur adipiscing</h3>
  <p>Sed ut perspiciatis unde omnis iste natus error sit voluptatem accusantium doloremque laudantium, totam rem aperiam, eaque ipsa quae ab illo inventore veritatis.</p>
  <div class="btn">Read More</div>
</article>
<article class="post" style="left:771px">
  <div class="thumb" role="img" aria-label="Hand touching a hexagon diagram labelled consulting" style="background:linear-gradient(135deg,#4a6180,#8aa0bd 55%,#c9d6e6)"></div>
  <div class="date">27 June 2023</div>
  <h3>Lorem ipsum dolor sit amet consectetur adipiscing</h3>
  <p>Sed ut perspiciatis unde omnis iste natus error sit voluptatem accusantium doloremque laudantium, totam rem aperiam, eaque ipsa quae ab illo inventore veritatis.</p>
  <div class="btn">Read More</div>
</article>

<footer class="site-footer">
  <div class="footer-brand"><span class="brand-mark"></span>Marrowgate Concepts LLC</div>

  <div class="footer-col"><h4 style="left:414px">CONTACT US</h4><div class="line" style="left:414px;width:192px"></div></div>
  <div class="f-item" style="left:414px;top:90px"><span class="f-icon"><svg width="10" height="12" viewBox="0 0 10 12"><path d="M5 0a4 4 0 0 0-4 4c0 3 4 8 4 8s4-5 4-8a4 4 0 0 0-4-4z" fill="#fff"/><circle cx="5" cy="4" r="1.5" fill="#0b3f86"/></svg></span><span>Lindqvist Lane 48<br>331 07 Tampa Bay</span></div>
  <div class="f-item" style="left:414px;top:141px"><span class="f-icon"><svg width="11" height="11" viewBox="0 0 11 11"><path d="M2 0l2 2.5-1.2 1.5a7 7 0 0 0 4.2 4.2L8.5 7 11 9l-1.5 2C5 11 0 6 0 1.5z" fill="#fff"/></svg></span><span>Call Us<br>+1 555 014 2760</span></div>
  <div class="f-item" style="left:414px;top:192px"><span class="f-icon"><svg width="12" height="9" viewBox="0 0 12 9"><rect width="12" height="9" fill="#fff"/><path d="M0 0l6 5 6-5" fill="none" stroke="#0b3f86"/></svg></span><span>E mail Us<br>hello@marrowgateconcepts.com</span></div>

  <div class="footer-col"><h4 style="left:699px">MENU</h4><div class="line" style="left:699px;width:106px"></div></div>
  <ul class="menu-list"><li>HOME</li><li>ABOUT US</li><li>SERVICES</li><li>BLOG</li><li>CONTACT US</li></ul>

  <div class="footer-col"><h4 style="left:916px">FOLLOW US</h4><div class="line" style="left:916px;width:108px"></div></div>
  <div class="f-item" style="left:916px;top:92px"><span class="f-icon"></span><span>Like us on<br>CIRCLEBOARD</span></div>
  <div class="f-item" style="left:916px;top:142px"><span class="f-icon"></span><span>Follow us on<br>CHIRPLINE</span></div>
  <div class="f-item" style="left:916px;top:193px"><span class="f-icon"></span><span>Follow us on<br>WORKLINKS</span></div>

  <div class="footer-divider"></div>
  <div class="copyright">Copyright © 2023 All Rights Reserved</div>
</footer>

</body>
</html>
```